New Business Card Design Project

Looking for a modern business card design for an import distribution business for industrial technical products. The winning design will translate modern, sophistication, technical, professional and sustainable.

Target Market(s)

Technical customers

Industry/Entity Type

Business

Contact Information for Business Card

Dean Harlow
Sales Manager
M: 0471 625 183
P: 1300 872 619
dean@volkarsystems.com.au
4/18 Galloway Crest Road
Marden Vale NSW 2168
www.volkarsystems.com.au

Font styles to use
Sans Serif

Colors
ec1f27
606060
000000
fbfbfb

Requirements
Must have
• My Logo which is the Volkar Systems logo attached
Nice to have
• Eurostile Bold font

```html
<!DOCTYPE html>
<html lang="en">
<head>
<meta charset="utf-8">
<title>Volkar Systems – Business Card</title>
<link rel="stylesheet" href="https://fonts.googleapis.com/css2?family=Open+Sans:wght@400;600;700&display=swap">
<style>
  :root {
    --brand-red: #ec1f27;
    --card-red-top: #d9453b;
    --card-red-bottom: #c81d14;
    --card-back-red: #d93226;
    --text-light: #fbfbfb;
    --stage: #ececec;
  }
  html, body {
    margin: 0;
    padding: 0;
    width: 1200px;
    height: 900px;
    overflow: hidden;
    background: var(--stage);
    font-family: "Open Sans", Arial, sans-serif;
  }
  .canvas {
    position: relative;
    width: 1200px;
    height: 900px;
  }
  .card {
    position: absolute;
    box-shadow: 0 6px 18px rgba(0,0,0,0.18);
    color: var(--text-light);
  }
  .card-front {
    left: 238px;
    top: 62px;
    width: 555px;
    height: 342px;
    background: linear-gradient(180deg, var(--card-red-top) 0%, var(--card-red-bottom) 100%);
  }
  .card-back {
    left: 457px;
    top: 518px;
    width: 560px;
    height: 343px;
    background: var(--card-back-red);
  }
  .brand-name {
    font-weight: 700;
    color: var(--text-light);
    white-space: nowrap;
    letter-spacing: 0.5px;
  }
  .card-front .brand-name {
    position: absolute;
    right: 36px;
    top: 58px;
    font-size: 36px;
    line-height: 1;
  }
  .contact-name {
    position: absolute;
    left: 34px;
    top: 134px;
    margin: 0;
    font-size: 17px;
    font-weight: 700;
  }
  .contact-title {
    position: absolute;
    left: 34px;
    top: 156px;
    margin: 0;
    font-size: 14px;
  }
  .address {
    position: absolute;
    left: 34px;
    top: 189px;
    margin: 0;
    font-size: 14px;
    line-height: 20px;
    font-style: normal;
  }
  .contact-list {
    position: absolute;
    left: 34px;
    top: 242px;
    margin: 0;
    padding: 0;
    list-style: none;
    font-size: 14px;
    line-height: 20px;
  }
  .contact-list li {
    display: flex;
    align-items: center;
  }
  .contact-icon {
    width: 11px;
    height: 11px;
    margin-right: 9px;
    fill: var(--text-light);
  }
  .back-lockup {
    position: absolute;
    left: 0;
    right: 0;
    top: 0;
    bottom: 0;
    display: flex;
    align-items: center;
    justify-content: center;
    gap: 18px;
  }
  .back-lockup .mark {
    width: 60px;
    height: 60px;
    background: var(--text-light);
  }
  .back-lockup .brand-name {
    font-size: 46px;
  }
</style>
</head>
<body>
<main class="canvas">
  <section class="card card-front" aria-label="Business card front">
    <div class="brand-name">Volkar Systems</div>
    <h1 class="contact-name">Dean Harlow</h1>
    <p class="contact-title">Sales Manager</p>
    <address class="address">4/18 Galloway Crest Road<br>Marden Vale NSW 2168</address>
    <ul class="contact-list">
      <li>
        <svg class="contact-icon" viewBox="0 0 12 12" aria-hidden="true"><path d="M3 0h6a1 1 0 0 1 1 1v10a1 1 0 0 1-1 1H3a1 1 0 0 1-1-1V1a1 1 0 0 1 1-1zm.5 1.5v7.5h5V1.5zM6 10a.6.6 0 1 0 0 1.2A.6.6 0 0 0 6 10z"/></svg>
        0471 625 183
      </li>
      <li>
        <svg class="contact-icon" viewBox="0 0 12 12" aria-hidden="true"><path d="M2.4 0.5l2 2.4-1.1 1.4a7 7 0 0 0 4.4 4.4l1.4-1.1 2.4 2-1.2 1.9C5.6 11.5.5 6.4.5 1.7z"/></svg>
        1300 872 619
      </li>
      <li>
        <svg class="contact-icon" viewBox="0 0 12 12" aria-hidden="true"><path d="M0 2.5h12v7H0zM.8 3.2L6 7l5.2-3.8v-.2H.8z"/></svg>
        dean@volkarsystems.com.au
      </li>
      <li>
        <svg class="contact-icon" viewBox="0 0 12 12" aria-hidden="true"><path d="M6 0a6 6 0 1 0 0 12A6 6 0 0 0 6 0zm-1 2.2l1.6 1.4-.8 1.4 1.8 1.2.2 2-1.4 1.6L5.6 8 4 7.2 3 5l1-1.4z"/></svg>
        www.volkarsystems.com.au
      </li>
    </ul>
  </section>

  <section class="card card-back" aria-label="Business card back">
    <div class="back-lockup">
      <span class="mark" aria-hidden="true"></span>
      <span class="brand-name">Volkar Systems</span>
    </div>
  </section>
</main>
</body>
</html>
```